Autism Support Coach needs Advertisement Design

I need an ad that fits in the feel of the "Save the Date" picture attached below. My business will be a sponsor and also advertising in the gala's magazine. I would like my original colors of orange and maroon red to be the standout colors. Phone number, website and Chatterfold should be somewhere at the bottom maybe. I am open to variations of background color in the oranges and maroon reds if you think it will look good. Dimensions should be: 4-1/2”h x 6” w
Thank you!!!

Target Market(s)

Autism Fundraising Gala with a Ruby theme

Industry/Entity Type

Advertising

Font styles to use
Script

Requirements
Must have
• The tag line should be:
• Autism Support Coaching
• Phone: 734-615-2089
• torvelancoaching.com
• Follow us on Chatterfold.com/Torvelancoachingautism

```html
<!DOCTYPE html>
<html lang="en">
<head>
<meta charset="utf-8">
<title>Torvelan Coaching Services – Autism Support Coaching</title>
<link rel="stylesheet" href="https://fonts.googleapis.com/css2?family=Dancing+Script:wght@700&family=Montserrat:wght@500;600;700;800&family=Open+Sans:wght@400;600&display=swap">
<style>
  :root {
    --cream: #f3ece0;
    --paper: #fdf8ee;
    --orange: #f07a1c;
    --orange-deep: #e8611a;
    --orange-light: #f7a957;
    --maroon: #b3162c;
    --red: #d42a2a;
    --ink: #3b3b3b;
    --white: #ffffff;
  }
  html, body {
    margin: 0;
    padding: 0;
    overflow: hidden;
    background: var(--cream);
  }
  .ad {
    position: relative;
    width: 1200px;
    height: 900px;
    overflow: hidden;
    background: var(--paper);
    font-family: "Open Sans", Arial, sans-serif;
  }
  .ad__backdrop {
    position: absolute;
    inset: 0;
  }
  .ad__phone {
    position: absolute;
    top: 22px;
    right: 34px;
    margin: 0;
    font-family: "Montserrat", Arial, sans-serif;
    font-weight: 500;
    font-size: 58px;
    letter-spacing: 1px;
    color: var(--white);
  }
  .feelings {
    position: absolute;
    top: 172px;
    left: 100px;
    width: 1000px;
    text-align: center;
  }
  .feelings__title {
    margin: 0 0 16px;
    font-family: "Montserrat", Arial, sans-serif;
    font-weight: 800;
    font-size: 44px;
    color: var(--maroon);
  }
  .feeling {
    margin: 0 0 12px;
  }
  .feeling__name {
    margin: 0;
    font-family: "Montserrat", Arial, sans-serif;
    font-weight: 700;
    font-size: 29px;
    line-height: 1.2;
    color: var(--orange-deep);
  }
  .feeling__text {
    margin: 0;
    font-size: 27px;
    line-height: 1.32;
    color: var(--ink);
  }
  .ad__cta {
    position: absolute;
    top: 640px;
    right: 90px;
    margin: 0;
    font-family: "Montserrat", Arial, sans-serif;
    font-weight: 700;
    font-size: 46px;
    color: var(--maroon);
  }
  .brand {
    position: absolute;
    left: 20px;
    top: 562px;
    width: 440px;
    text-align: center;
  }
  .brand__dot {
    display: block;
    width: 150px;
    height: 150px;
    margin: 0 0 0 77px;
    border-radius: 50%;
    background: var(--white);
  }
  .brand__name {
    margin: 4px 0 0;
    font-family: "Dancing Script", cursive;
    font-weight: 700;
    font-size: 70px;
    line-height: 1;
    color: var(--white);
    text-align: left;
    padding-left: 20px;
  }
  .brand__tag {
    margin: 6px 0 0;
    font-family: "Montserrat", Arial, sans-serif;
    font-weight: 600;
    font-size: 22px;
    letter-spacing: 3px;
    color: var(--white);
    text-align: left;
    padding-left: 20px;
  }
  .contact {
    position: absolute;
    right: 40px;
    bottom: 26px;
    text-align: right;
  }
  .contact__web {
    margin: 0;
    font-family: "Montserrat", Arial, sans-serif;
    font-weight: 500;
    font-size: 40px;
    color: var(--white);
  }
  .contact__social {
    margin: 4px 0 0;
    font-family: "Montserrat", Arial, sans-serif;
    font-weight: 500;
    font-size: 20px;
    color: var(--white);
  }
</style>
</head>
<body>
  <main class="ad">
    <svg class="ad__backdrop" width="1200" height="900" viewBox="0 0 1200 900" aria-hidden="true">
      <defs>
        <linearGradient id="top-band" x1="0" y1="0" x2="1" y2="0">
          <stop offset="0" stop-color="#f6a24e"/>
          <stop offset="1" stop-color="#ef6f1b"/>
        </linearGradient>
        <linearGradient id="lower-band" x1="0" y1="0" x2="1" y2="0">
          <stop offset="0" stop-color="#f07a1c"/>
          <stop offset="0.5" stop-color="#f7a957"/>
          <stop offset="1" stop-color="#f08a2c"/>
        </linearGradient>
        <linearGradient id="base-band" x1="0" y1="0" x2="1" y2="0">
          <stop offset="0" stop-color="#f28a2a"/>
          <stop offset="1" stop-color="#e8611a"/>
        </linearGradient>
      </defs>
      <path class="top-stripe" d="M120,0 H1200 V170 C900,140 520,40 120,0 Z" fill="var(--red)"/>
      <path class="top-band" d="M150,0 H1200 V148 C900,118 540,28 150,0 Z" fill="url(#top-band)"/>
      <path class="lower-stripe" d="M0,612 C400,572 800,590 1200,545 V900 H0 Z" fill="var(--red)"/>
      <path class="lower-band" d="M0,628 C400,590 800,606 1200,562 V900 H0 Z" fill="url(#lower-band)"/>
      <path class="base-stripe" d="M0,790 C420,720 820,770 1200,700 V900 H0 Z" fill="var(--red)"/>
      <path class="base-band" d="M0,806 C420,738 820,788 1200,718 V900 H0 Z" fill="url(#base-band)"/>
      <path class="brand-wave" d="M0,628 C150,620 330,650 450,900 H0 Z" fill="var(--orange)"/>
    </svg>

    <p class="ad__phone">734.615.2089</p>

    <section class="feelings">
      <h1 class="feelings__title">ARE YOU FEELING:</h1>
      <div class="feeling">
        <h2 class="feeling__name">Overwhelmed?</h2>
        <p class="feeling__text">Your child's behavior seems unmanageable, it's over the top and<br>you're at your wit's end?</p>
      </div>
      <div class="feeling">
        <h2 class="feeling__name">Helpless?</h2>
        <p class="feeling__text">When your child acts out in public and people<br>disapprove or stare?</p>
      </div>
      <div class="feeling">
        <h2 class="feeling__name">Anxious?</h2>
        <p class="feeling__text">You don't know what will happen to your child if<br>something happens to you?</p>
      </div>
    </section>

    <p class="ad__cta">I can help!</p>

    <div class="brand">
      <span class="brand__dot"></span>
      <p class="brand__name">Torvelan</p>
      <p class="brand__tag">AUTISM SUPPORT COACHING</p>
    </div>

    <div class="contact">
      <p class="contact__web">www.torvelancoaching.com</p>
      <p class="contact__social">Follow us on Chatterfold.com/Torvelancoachingautism</p>
    </div>
  </main>
</body>
</html>
```